Not your average candle company needs label design

MOSS + RUIN A Brand Deck for Disruptive Candles
WHO WE ARE
Moss + Ruin is a disruptive candle brand built on contrast. We create clean-burning, scent-forward rituals for people who are both grounded and undone.
We’re not here for the beige wellness aesthetic. We’re here for the moments that are messy, bold, emotional, and beautifully real.
Rooted in botanical craftsmanship. Branded in poetic defiance.
WHAT WE WANT PEOPLE TO THINK
When someone encounters Moss + Ruin, we want them to feel like they’ve stumbled into something intimate, moody, and unforgettable.
We want them to think:
• “This brand gets me.”
• “This feels like design, emotion, and scent in one.”
• “It’s art I can burn.”
• “I’ve never seen a candle brand like this before.”
Our name alone sparks curiosity. Our story keeps them. Our product delivers.

Target Market(s)

Women and men ages 25–45 who appreciate thoughtful design and emotional storytelling People who love brands like Velmoria, Kid Scents, Heron Grange, Miravo, and La Fiole Design-minded buyers who shop indie, high-end, or artisanal and care about self-expression through scent Emotionally intelligent rebels. Introspective, edgy, but craving grounding rituals.

Industry/Entity Type

Candle Industry

Font styles to use
Other font styles liked:
• Moss should be more refined in a serif font and I like mistrully font for ruin.

Requirements
Must have
• Space for scent name and optionally, a small poetic tagline (like quiet ember. loud bloom.) Layout that’s elegant but with tension — surprise us with something that doesn't play it safe Optional: room for batch no., burn time, scent notes on side or bottom. MOSS + RUIN quiet ember. loud bloom. Scent name example: Troth Warden A silent vow to stay grounded. Earthy and grounding — like old books, soft shadows, and the quiet certainty of knowing who you are. [optional: 7 oz / 198g | coconut soy wax | 45+ hr burn time]
Nice to have
• raw edge opening with gold font. Open to colored labels. We’re creating an unforgettable candle brand called Moss + Ruin — a contrast-rich, emotionally resonant collection of candles that blend botanical beauty with bold edge. The name is intentional: Moss reflects grounding, ritual, and plant-based purity; Ruin speaks to vulnerability, chaos, and strength through contrast. Our brand is not dark or gothic — it’s confident, elevated, and style-forward, with packaging that feels like a cross between modern apothecary and high fashion. Think Miravo meets Dane Pellor. Gloss vessels, textured labels, contrasting fonts, and emotional scent storytelling.
Should not have
• goth vibe, typical candle label template layout.

```html
<!DOCTYPE html>
<html lang="en">
<head>
<meta charset="utf-8">
<title>Moss + Ruin — Troth Warden Label</title>
<link rel="stylesheet" href="https://fonts.googleapis.com/css2?family=Cormorant+SC:wght@600&family=Montserrat:wght@500;600;800&family=Open+Sans:wght@600&display=swap">
<style>
  :root {
    --backdrop: #d9d9d9;
    --label-white: #ffffff;
    --panel-black: #121212;
    --gold: #c9a544;
    --ink: #111111;
  }
  * { margin: 0; padding: 0; box-sizing: border-box; }
  html, body {
    width: 1200px; height: 1200px; overflow: hidden;
    background: var(--backdrop);
  }
  .canvas {
    position: relative; width: 1200px; height: 1200px;
    display: flex; align-items: center; justify-content: center;
  }
  .label {
    position: relative; width: 960px; height: 800px;
    background: var(--label-white);
  }
  .label__panel {
    position: absolute; left: 0; top: 0; width: 100%; height: 535px;
    background: var(--panel-black);
    border-radius: 0 0 34px 34px;
    text-align: center; color: var(--gold);
  }
  .brand-name {
    position: absolute; top: 108px; left: 0; width: 100%;
    display: flex; align-items: center; justify-content: center; gap: 14px;
    font-family: "Montserrat", sans-serif; font-weight: 600;
    font-size: 38px; letter-spacing: 4px; color: var(--gold);
  }
  .brand-name__dot {
    width: 12px; height: 12px; border-radius: 50%;
    background: var(--gold);
  }
  .brand-tagline {
    position: absolute; top: 180px; left: 0; width: 100%;
    font-family: "Montserrat", sans-serif; font-weight: 500;
    font-size: 30px; letter-spacing: 1px; color: var(--gold);
  }
  .scent-title {
    position: absolute; top: 325px; left: 0; width: 100%; height: 130px;
  }
  .scent-title text {
    font-family: "Montserrat", sans-serif; font-weight: 800;
    font-size: 82px; fill: var(--gold);
  }
  .scent-vow {
    position: absolute; top: 452px; left: 0; width: 100%;
    font-family: "Open Sans", sans-serif; font-weight: 600;
    font-size: 26px; color: var(--gold); letter-spacing: -0.3px;
  }
  .scent-notes {
    position: absolute; top: 575px; left: 0; width: 100%;
    text-align: center;
    font-family: "Cormorant SC", serif; font-weight: 600;
    font-size: 24px; line-height: 30px; color: var(--ink);
  }
  .specs {
    position: absolute; top: 665px; left: 42px; right: 70px;
    display: flex; align-items: center; justify-content: space-between;
    font-family: "Montserrat", sans-serif; font-weight: 600;
    font-size: 30px; color: var(--ink);
  }
  .burn-badge {
    border: 3px solid var(--ink); border-radius: 8px;
    padding: 4px 8px 2px; text-align: center; line-height: 1;
  }
  .burn-badge__hours { font-size: 44px; font-weight: 800; }
  .burn-badge__hours small { font-size: 36px; font-weight: 600; }
  .burn-badge__caption { display: block; font-size: 20px; font-weight: 600; margin-top: 2px; }
</style>
</head>
<body>
<main class="canvas">
  <section class="label">
    <div class="label__panel">
      <div class="brand-name"><span class="brand-name__dot"></span><span>MOSS + RUIN</span></div>
      <div class="brand-tagline">quiet ember. loud bloom.</div>
      <svg class="scent-title" viewBox="0 0 960 130" aria-label="Troth Warden">
        <defs><path id="title-arc" d="M150 120 Q480 40 810 120"/></defs>
        <text text-anchor="middle"><textPath href="#title-arc" startOffset="50%" textLength="650" lengthAdjust="spacingAndGlyphs">TROTH WARDEN</textPath></text>
      </svg>
      <div class="scent-vow">A SILENT VOW TO STAY GROUNDED.</div>
    </div>
    <p class="scent-notes">Earthy and grounding—like old books, soft shadows,<br>and the quiet certainty of knowing who you are.</p>
    <div class="specs">
      <span class="specs__wax">Coconut Soy Wax</span>
      <span class="burn-badge"><span class="burn-badge__hours">45+<small>hr</small></span><span class="burn-badge__caption">BURN TIME</span></span>
      <span class="specs__weight">7 oz / 198g</span>
    </div>
  </section>
</main>
</body>
</html>
```